Design a business card for Harbor Profile

I need a business card designed for a new company called HarborProfile.example . I will be doing a lot of networking and the business card is the first thing people will see. I need to get them to my website. I already have a logo and attached it here.
A Harbor Profile is a personal website with career tools to promote your professional success. For more information, visit HarborProfile.example .

My tag line is Stride Out-and Prevail although if there is room, I would rather use - Don't leave your career up to someone else. Stride Out-and Prevail.

My target customer is the professional who is successful at their job but needs to get to the next level in their career. Essentially, everyone on Workmesh.example that does not own their own company.

Other information for the card:

Ned Varcoe
CEO

555-014-7732

Ned@HarborProfile.example

HarborProfile.example

I need a high resolution deign ready to print. I also need the original PSD files.

Target Market(s)

Professionals in the growth phase of their career

Industry/Entity Type

Business

Contact Information for Business Card

Don't leave your career up to someone else. Stride Out-and Prevail.

Ned Varcoe
CEO

555-014-7732

Ned@HarborProfile.example

HarborProfile.example

Font styles to use
Serif

Requirements
Must have
• My log and original colors, Images and it has to be fun and very impressive

```html
<!DOCTYPE html>
<html lang="en">
<head>
<meta charset="utf-8">
<title>Harbor Profile — Business Card</title>
<link rel="stylesheet" href="https://fonts.googleapis.com/css2?family=Bodoni+Moda:ital,opsz,wght@0,6..96,400;0,6..96,600;1,6..96,700&display=swap">
<style>
  :root {
    --stage: #d9d9db;
    --navy: #1a2132;
    --navy-deep: #121826;
    --navy-light: #2a3450;
    --pink: #e4186a;
    --pink-bright: #f0307f;
    --white: #ffffff;
    --paper: #f4f4f6;
  }
  * { box-sizing: border-box; margin: 0; padding: 0; }
  html, body {
    width: 1200px;
    height: 900px;
    overflow: hidden;
    background: var(--stage);
  }
  .canvas {
    position: relative;
    width: 1200px;
    height: 900px;
    font-family: "Bodoni Moda", "Libre Bodoni", serif;
  }
  .card {
    position: absolute;
    left: 250px;
    width: 700px;
    height: 400px;
    overflow: hidden;
    box-shadow: 0 6px 18px rgba(0, 0, 0, 0.18);
  }

  /* Front */
  .card--front {
    top: 40px;
    background: linear-gradient(135deg, var(--navy-deep) 0%, var(--navy) 55%, var(--navy-light) 100%);
    color: var(--white);
  }
  .card__name {
    position: absolute;
    left: 44px;
    top: 50px;
    font-size: 34px;
    font-weight: 400;
    letter-spacing: 2px;
    line-height: 1;
    text-transform: uppercase;
  }
  .card__rule {
    position: absolute;
    left: 44px;
    top: 98px;
    width: 340px;
    height: 2px;
    background: var(--pink);
  }
  .card__title {
    position: absolute;
    left: 366px;
    top: 102px;
    font-size: 13px;
    line-height: 1;
    letter-spacing: 7px;
    color: var(--pink);
  }
  .card__phone {
    position: absolute;
    left: 0;
    right: 0;
    top: 146px;
    text-align: center;
    font-size: 44px;
    line-height: 1;
    font-weight: 600;
    letter-spacing: 15px;
    color: var(--pink);
  }
  .card__contact {
    position: absolute;
    right: 40px;
    top: 240px;
    font-size: 17px;
    line-height: 1;
    letter-spacing: 0.3px;
  }
  .card__contact .divider {
    color: var(--pink);
    margin: 0 10px;
  }
  .card__band {
    position: absolute;
    left: 0;
    right: 0;
    bottom: 0;
    height: 78px;
    background: var(--pink);
    display: flex;
    align-items: center;
    justify-content: center;
  }
  .card__tagline {
    font-size: 17px;
    font-style: italic;
    font-weight: 700;
    color: var(--white);
    letter-spacing: 0.3px;
    white-space: nowrap;
  }

  /* Back */
  .card--back {
    top: 470px;
    background: linear-gradient(135deg, var(--pink) 0%, var(--pink-bright) 100%);
  }
  .card__field {
    position: absolute;
    left: 0;
    top: 0;
    width: 620px;
    height: 320px;
    background: var(--paper);
  }
  .brand {
    position: absolute;
    left: 70px;
    top: 112px;
    display: flex;
    align-items: center;
    gap: 16px;
  }
  .brand__dot {
    width: 26px;
    height: 26px;
    border-radius: 50%;
    background: var(--pink);
  }
  .brand__name {
    font-size: 50px;
    line-height: 1;
    font-weight: 600;
    color: var(--navy);
    letter-spacing: 1px;
  }
  .brand__url {
    position: absolute;
    left: 112px;
    top: 196px;
    font-size: 22px;
    line-height: 1;
    font-weight: 600;
    letter-spacing: 3px;
    color: var(--pink);
  }
</style>
</head>
<body>
<main class="canvas">

  <section class="card card--front" aria-label="Business card front">
    <h1 class="card__name">Ned Varcoe</h1>
    <div class="card__rule"></div>
    <p class="card__title">CEO</p>
    <p class="card__phone">555-014-7732</p>
    <p class="card__contact">Ned@HarborProfile.example<span class="divider">|</span>HarborProfile.example</p>
    <div class="card__band">
      <p class="card__tagline">Don't leave your career up to someone else. Stride Out - and Prevail.</p>
    </div>
  </section>

  <section class="card card--back" aria-label="Business card back">
    <div class="card__field"></div>
    <div class="brand">
      <span class="brand__dot"></span>
      <span class="brand__name">Harbor Profile</span>
    </div>
    <p class="brand__url">harborprofile.example</p>
  </section>

</main>
</body>
</html>
```